New Business card design to reflect rebrand

I would like a business card design with a good base colour for our new logo and also a placeholder for a profile pic of the card holder. the design needs to be editable to the point that we can easily change the picture of the person and use that design for printlarkly etc. we are looking at a metalic finish business card so will need a good base colour to bring out the finish.

Target Market(s)

prospective customers

Industry/Entity Type

Business

Contact Information for Business Card

I would like one editable design that we can change the name of the card holder and profile picture. The design need to be in a format that be send to printlarkly etc.

Our address is Fenwick Lodge, Mill Lane, Ashcombe Vale, KT14 3WB Tel no. 01632 960418

Requirements
Must have
• place holder for a profile pic for the card holder. in AI or preferably PSD format

```html
<!DOCTYPE html>
<html lang="en">
<head>
<meta charset="utf-8">
<title>Brightwell Workplace Services – Business Card</title>
<link href="https://fonts.googleapis.com/css2?family=Source+Sans+3:wght@400;600;700&display=swap" rel="stylesheet">
<style>
  :root {
    --navy: #435874;
    --orange: #ef6a22;
    --ink: #3f5069;
    --white: #ffffff;
    --backdrop: #4b3b45;
    --photo-light: #eeeeee;
    --photo-dark: #2b3142;
  }
  * { margin: 0; padding: 0; box-sizing: border-box; }
  html, body { width: 1200px; height: 1200px; overflow: hidden; }
  body {
    background: var(--backdrop);
    font-family: "Source Sans 3", sans-serif;
    position: relative;
  }
  .card {
    position: absolute;
    left: 235px;
    width: 728px;
    height: 412px;
    border-radius: 16px;
    overflow: hidden;
  }
  .card--front { top: 166px; background: var(--white); }
  .card--back { top: 621px; background: var(--navy); }

  .brand {
    position: absolute;
    left: 33px;
    top: 62px;
    display: flex;
    align-items: center;
    gap: 10px;
    color: var(--navy);
    font-weight: 700;
  }
  .brand__mark { width: 16px; height: 16px; background: var(--orange); }
  .brand__name { font-size: 36px; line-height: 1; letter-spacing: 1px; }
  .brand__sub {
    position: absolute;
    left: 34px;
    top: 107px;
    color: var(--orange);
    font-weight: 600;
    font-size: 13px;
    line-height: 1;
    letter-spacing: 3.2px;
  }

  .holder__bar {
    position: absolute;
    left: 0;
    top: 163px;
    width: 14px;
    height: 52px;
    background: var(--orange);
  }
  .holder__name {
    position: absolute;
    left: 28px;
    top: 163px;
    color: var(--orange);
    font-size: 28px;
    font-weight: 400;
    line-height: 1;
  }
  .holder__title {
    position: absolute;
    left: 28px;
    top: 195px;
    color: var(--ink);
    font-size: 19.5px;
  }
  .address {
    position: absolute;
    left: 28px;
    top: 228px;
    color: var(--ink);
    font-size: 19.5px;
    line-height: 24px;
  }
  .contacts {
    position: absolute;
    left: 28px;
    top: 284px;
    list-style: none;
    color: var(--ink);
    font-size: 19.5px;
    line-height: 24.5px;
  }
  .contacts li { display: flex; align-items: center; gap: 9px; }
  .contacts svg { width: 15px; height: 15px; flex: none; }

  .photo {
    position: absolute;
    left: 457px;
    top: 0;
    width: 271px;
    height: 360px;
    background: linear-gradient(160deg, var(--photo-light) 0%, var(--photo-light) 35%, var(--photo-dark) 100%);
  }
  .wave { position: absolute; left: 0; top: 0; width: 728px; height: 412px; }

  .back__brand {
    position: absolute;
    left: 0;
    right: 0;
    top: 166px;
    text-align: center;
    color: var(--white);
    font-weight: 700;
    font-size: 64px;
    line-height: 1;
    letter-spacing: 2px;
  }
  .back__web {
    position: absolute;
    left: 0;
    right: 0;
    top: 344px;
    text-align: center;
    color: var(--white);
    font-size: 19.5px;
  }
</style>
</head>
<body>

<section class="card card--front">
  <div class="photo" role="img" aria-label="Profile photo of the card holder"></div>

  <svg class="wave" viewBox="0 0 728 412" aria-hidden="true">
    <path d="M170,400 C360,392 560,338 728,328 L728,342 C560,347 360,392 170,400 Z" fill="var(--orange)"/>
    <path d="M0,366 C60,390 130,402 210,400 C380,396 560,352 728,349 L728,412 L0,412 Z" fill="var(--navy)"/>
  </svg>

  <div class="brand">
    <span class="brand__mark"></span>
    <span class="brand__name">BRIGHTWELL</span>
  </div>
  <div class="brand__sub">WORKPLACE SERVICES</div>

  <span class="holder__bar"></span>
  <h1 class="holder__name">Marcus Hale</h1>
  <p class="holder__title">Managing Parter</p>

  <p class="address">Fenwick Lodge, Mill Lane<br>Ashcombe Vale, KT14 3WB</p>

  <ul class="contacts">
    <li>
      <svg viewBox="0 0 16 16"><path d="M1 6c0-2 3-3 7-3s7 1 7 3v1h-3.5V5.5h-7V7H1z M4 8h8l2 5H2z" fill="var(--orange)"/><circle cx="8" cy="10.5" r="1.6" fill="var(--white)"/></svg>
      01632 960418
    </li>
    <li>
      <svg viewBox="0 0 16 16"><rect x="1" y="3.5" width="14" height="9" fill="var(--orange)"/><path d="M1 3.5l7 5 7-5" fill="none" stroke="var(--white)" stroke-width="1.2"/></svg>
      mhale@brightwellwork.com
    </li>
    <li>
      <svg viewBox="0 0 16 16" fill="none" stroke="var(--orange)" stroke-width="1.3"><circle cx="8" cy="8" r="6.5"/><ellipse cx="8" cy="8" rx="3" ry="6.5"/><path d="M1.5 8h13M2.5 4.8h11M2.5 11.2h11"/></svg>
      www.brightwellwork.com
    </li>
  </ul>
</section>

<section class="card card--back">
  <div class="back__brand">BRIGHTWELL</div>
  <p class="back__web">www.brightwellwork.com</p>
</section>

</body>
</html>
```